Preferred pricing vendor

We are a plumbing company that has many services
-Boilers & Controls
-Plumbing & Heating
-HVAC & Refrigeration
-Preventative Maintenacne
-Gas fitting & Drain Cleaning

We primarily look after condo buildings, and our preferred service rates ($98, $93, or $88 depending on the contract) extend to all of our clients. So in essence, we look after the mechanical room and common equipment but our clients can call us in for drain cleaning or replacing a fixture in their suite. The discounted rates apply to the personal residence. We want a flyer to let them know they get a discount on our services. A one-pager we can send out to all of our contract clients.

Included source files for our letterhead and logo just so you can see the colours we go with.

Target Market(s)

Residential repairs, individual people, replacement of fixtures in-suite specific repairs

Requirements
Must have
• be colourful and attractive

```html
<!DOCTYPE html>
<html lang="en">
<head>
<meta charset="utf-8">
<title>Keystone Mechanical Inc – Resident Rates Flyer</title>
<link href="https://fonts.googleapis.com/css2?family=Montserrat:wght@300;500;600;700;800&display=swap" rel="stylesheet">
<style>
  :root{
    --brand-blue:#1a6cbf;
    --brand-blue-deep:#145aa3;
    --brand-orange:#f05a28;
    --ink-navy:#0f1f3d;
    --paper:#ffffff;
    --stage:#2d2d30;
    --shadow:rgba(0,0,0,.28);
  }
  *{margin:0;padding:0;box-sizing:border-box}
  html,body{width:920px;height:1200px;overflow:hidden;background:var(--stage)}
  body{font-family:"Montserrat",sans-serif}
  .flyer{position:absolute;left:35px;top:0;width:850px;height:1200px;background:var(--paper);overflow:hidden}
  .flyer-shapes{position:absolute;inset:0}
  .brand{position:absolute;left:20px;top:95px;width:340px;text-align:center;color:var(--paper)}
  .brand-mark{width:120px;height:120px;border-radius:50%;background:var(--brand-orange);margin:0 auto 22px}
  .brand-name{font-weight:800;font-size:46px;line-height:1;letter-spacing:1px}
  .brand-name small{display:block;font-size:19px;letter-spacing:3px;margin-top:8px}
  .offer-bubble{position:absolute;left:47px;top:388px;width:254px;height:208px;background:var(--brand-orange);border-radius:30px;color:var(--paper);font-weight:800;font-size:28px;line-height:35px;text-align:center;display:flex;align-items:center;justify-content:center}
  .offer-bubble::after{content:"";position:absolute;left:100px;bottom:-30px;border-left:26px solid transparent;border-right:26px solid transparent;border-top:32px solid var(--brand-orange)}
  .offer-shadow{position:absolute;left:124px;top:640px;width:102px;height:20px;border-radius:50%;background:#e3e3e3}
  .services{position:absolute;top:692px;list-style:none;color:var(--brand-blue);font-weight:700;font-size:30px;line-height:38px}
  .services.left{left:123px}
  .services.right{left:535px}
  .services li{position:relative}
  .services .bullet::before{content:"";position:absolute;left:-38px;top:10px;width:20px;height:20px;border-radius:50%;border:4px solid var(--brand-orange);background:var(--brand-blue)}
  .rates{position:absolute;left:68px;top:872px;width:714px;height:195px;background:var(--brand-orange);border-radius:20px;display:flex}
  .rate{flex:1;text-align:center;color:var(--paper);position:relative;padding-top:10px}
  .rate + .rate{border-left:2px dotted var(--ink-navy)}
  .rate h3{font-weight:800;font-size:16px;letter-spacing:.5px}
  .rate p{font-weight:500;font-size:13.5px;line-height:18px;margin-top:6px}
  .rate-price{position:absolute;left:50%;top:92px;transform:translateX(-50%);width:108px;height:108px;border-radius:50%;background:var(--paper);box-shadow:0 6px 14px var(--shadow);display:flex;align-items:center;justify-content:center;font-weight:800;font-size:34px;color:var(--ink-navy)}
  .office{position:absolute;left:118px;top:1104px;color:var(--paper);display:flex;gap:16px;align-items:center}
  .office h4{font-weight:300;font-size:27px;line-height:30px}
  .office p{font-weight:700;font-size:17px;letter-spacing:2px;margin-top:2px}
  .contact{position:absolute;left:560px;top:1106px;width:230px;text-align:center;color:var(--paper)}
  .social{display:flex;justify-content:center;gap:36px;margin-bottom:14px}
  .social span{width:24px;height:24px;border-radius:50%;border:3px solid var(--brand-orange)}
  .web{font-weight:700;font-size:17px;letter-spacing:2px}
</style>
</head>
<body>
<main class="flyer">
  <svg class="flyer-shapes" width="850" height="1200" viewBox="0 0 850 1200">
    <defs>
      <linearGradient id="photoTone" x1="0" y1="0" x2="1" y2="1">
        <stop offset="0" stop-color="#d9d6d2"/>
        <stop offset=".5" stop-color="#2d4f8f"/>
        <stop offset="1" stop-color="#1d3f7d"/>
      </linearGradient>
      <linearGradient id="pipeTone" x1="0" y1="0" x2="1" y2="1">
        <stop offset="0" stop-color="#e8e8e8"/><stop offset="1" stop-color="#9aa0a6"/>
      </linearGradient>
      <linearGradient id="fitterTone" x1="0" y1="0" x2="1" y2="1">
        <stop offset="0" stop-color="#d8d2c6"/><stop offset="1" stop-color="#2552a8"/>
      </linearGradient>
    </defs>
    <rect class="hero-photo" x="0" y="0" width="850" height="640" fill="url(#photoTone)" role="img" aria-label="Photo of a plumber in blue overalls and gloves holding a pipe wrench, with a tool belt"/>
    <path class="hero-panel" d="M0,0 H433 C452,180 405,395 300,458 C205,512 85,515 0,505 Z" fill="var(--brand-blue)"/>
    <path class="swoosh-orange" d="M850,290 C805,420 660,520 480,560 L300,572 L300,612 C520,606 710,560 850,470 Z" fill="var(--brand-orange)"/>
    <path class="swoosh-blue" d="M850,470 C720,560 560,605 300,612 L300,630 C560,630 740,590 850,535 Z" fill="var(--brand-blue)"/>
    <path class="lower-field" d="M0,505 C140,560 340,612 500,628 C640,640 760,590 850,540 V1200 H0 Z" fill="var(--paper)"/>
    <path d="M300,360 C330,300 350,250 360,200" fill="none" stroke="#fff" stroke-width="3" stroke-dasharray="1 9" stroke-linecap="round"/>
    <circle cx="459" cy="580" r="103" fill="var(--brand-orange)"/>
    <circle cx="459" cy="580" r="88" fill="url(#pipeTone)" role="img" aria-label="Photo of gloved hands tightening a chrome sink trap with a wrench"/>
    <circle cx="711" cy="531" r="124" fill="var(--brand-orange)"/>
    <circle cx="711" cy="531" r="107" fill="url(#fitterTone)" role="img" aria-label="Photo of a smiling plumber in blue overalls working under a kitchen sink"/>
    <path class="footer-swoosh" d="M0,1000 L110,940 L110,1070 L0,1070 Z M850,1000 L740,940 L740,1070 L850,1070 Z" fill="var(--brand-orange)"/>
    <rect class="footer" x="0" y="1065" width="850" height="135" fill="var(--brand-blue)"/>
    <path d="M0,1020 L110,950 L110,1065 L0,1065 Z" fill="var(--brand-orange)"/>
    <path d="M850,1020 L740,950 L740,1065 L850,1065 Z" fill="var(--brand-orange)"/>
    <path d="M5,1175 C40,1130 70,1100 85,1080" fill="none" stroke="#fff" stroke-width="3" stroke-dasharray="1 9" stroke-linecap="round"/>
    <path d="M845,1175 C810,1130 780,1100 765,1080" fill="none" stroke="#fff" stroke-width="3" stroke-dasharray="1 9" stroke-linecap="round"/>
  </svg>

  <header class="brand">
    <div class="brand-mark"></div>
    <h1 class="brand-name">KEYSTONE<small>MECHANICAL INC</small></h1>
  </header>

  <div class="offer-bubble">The discounted<br>rates apply to<br>the personal<br>residence</div>
  <div class="offer-shadow"></div>

  <ul class="services left">
    <li class="bullet">Boilers &amp; Controls</li>
    <li class="bullet">Plumbing &amp; Heating</li>
    <li class="bullet">HVAC &amp;</li>
    <li>Refrigeration</li>
  </ul>
  <ul class="services right">
    <li class="bullet">Preventative</li>
    <li class="bullet">Maintenacne</li>
    <li>Gas fitting &amp;</li>
    <li>Drain Cleaning</li>
  </ul>

  <section class="rates">
    <div class="rate"><h3>YOUR TITLE</h3><p>Lorem ipsum dolor sit<br>amet, consectetuer.</p><div class="rate-price">$90</div></div>
    <div class="rate"><h3>YOUR TITLE</h3><p>Lorem ipsum dolor sit<br>amet, consectetuer.</p><div class="rate-price">$90</div></div>
    <div class="rate"><h3>YOUR TITLE</h3><p>Lorem ipsum dolor sit<br>amet, consectetuer.</p><div class="rate-price">$90</div></div>
  </section>

  <footer>
    <div class="office">
      <svg width="40" height="50" viewBox="0 0 40 50" aria-hidden="true"><path d="M20,0 C9,0 0,9 0,20 C0,33 20,50 20,50 C20,50 40,33 40,20 C40,9 31,0 20,0 Z M20,10 A10,10 0 1 1 19.9,10 Z" fill="#fff" fill-rule="evenodd"/></svg>
      <div><h4>Head Office</h4><p>St. Lorem No. 7, NY City</p></div>
    </div>
    <div class="contact">
      <div class="social"><span></span><span></span><span></span></div>
      <div class="web">WWW.YOURWEB.COM</div>
    </div>
  </footer>
</main>
</body>
</html>
```